Silver Heron Construction Services

Create a business card for my business consulting company
Danielle Vesk, Founder and CEO
4816 Alder Brook Way, Ste 100
Denver, CO. 80451
303.782.4190 cell
dvesk@silverheronconst.example
www.silverheronconst.example

Target Market(s)

Private Equity and Construction Companies

Industry/Entity Type

Business / Sales Consulting

Contact Information for Business Card

Tag Line that says "Where The Road To Success Is Always Under Construction"

Requirements
Must have
• Logo on both sides of the card.
Nice to have
• Add tagline to the same side of the card as my name and contact info

```html
<!DOCTYPE html>
<html lang="en">
<head>
<meta charset="utf-8">
<title>Silver Heron Construction Services – Business Card</title>
<link rel="stylesheet" href="https://fonts.googleapis.com/css2?family=Montserrat:wght@400;700&display=swap">
<style>
  :root {
    --stage: #3a3a3a;
    --card-black: #141414;
    --gloss: #2e2e2e;
    --card-white: #ffffff;
    --ink: #111111;
    --band: #0a0a0a;
    --paper-text: #ffffff;
  }
  * { box-sizing: border-box; margin: 0; padding: 0; }
  html, body {
    width: 1200px; height: 689px; overflow: hidden;
    background: var(--stage);
    font-family: "Montserrat", sans-serif;
  }
  .sheet {
    position: relative; width: 1200px; height: 689px;
    display: flex; align-items: center; justify-content: center; gap: 40px;
  }
  .card {
    position: relative; width: 540px; height: 309px;
    border-radius: 18px; overflow: hidden;
  }

  /* Back side */
  .card--back { background: var(--card-black); }
  .card--back .brand {
    position: absolute; left: 0; right: 0; top: 92px;
    display: flex; flex-direction: column; align-items: center; gap: 10px;
  }
  .card--back .brand-mark {
    width: 30px; height: 30px; border-radius: 50%; background: var(--gloss);
  }
  .card--back .brand-name {
    color: var(--gloss); font-weight: 700; font-size: 25px;
    text-transform: uppercase; text-align: center; line-height: 1.2;
    letter-spacing: 0.5px;
  }
  .card--back .tagline {
    position: absolute; left: 0; right: 0; bottom: 30px;
    text-align: center; color: var(--paper-text); font-size: 14px;
  }

  /* Front side */
  .card--front { background: var(--card-white); color: var(--ink); }
  .card--front .brand {
    position: absolute; right: 40px; top: 34px;
    display: flex; align-items: center; gap: 10px;
  }
  .card--front .brand-mark {
    width: 24px; height: 24px; border-radius: 50%; background: var(--ink);
  }
  .card--front .brand-name {
    font-weight: 700; font-size: 15px; text-transform: uppercase;
    line-height: 1.2; width: 180px;
  }
  .rule-top {
    position: absolute; left: 200px; right: 40px; top: 112px;
    height: 1px; background: var(--ink);
  }
  .person { position: absolute; left: 40px; top: 140px; }
  .person-name { font-weight: 700; font-size: 24px; line-height: 1.1; }
  .person-role { font-size: 15px; margin-top: 4px; }
  .rule-mid {
    position: absolute; left: 40px; width: 150px; top: 203px;
    height: 1px; background: var(--ink);
  }
  .contacts {
    position: absolute; left: 40px; top: 212px; list-style: none;
    font-size: 13px; line-height: 18px;
  }
  .contacts li { display: flex; align-items: center; gap: 9px; }
  .contacts svg { width: 13px; height: 13px; flex: none; }
  .address {
    position: absolute; right: 40px; top: 140px; text-align: right;
    font-size: 14px; line-height: 20px;
  }
  .band {
    position: absolute; left: 0; right: 0; bottom: 0; height: 34px;
    background: var(--band); color: var(--paper-text);
    font-size: 13px; display: flex; align-items: center; justify-content: center;
  }
</style>
</head>
<body>
<main class="sheet">
  <section class="card card--back" aria-label="Card back">
    <div class="brand">
      <span class="brand-mark"></span>
      <span class="brand-name">Silver Heron<br>Construction Services</span>
    </div>
    <p class="tagline">Where The Road To Success Is Always Under Construction</p>
  </section>

  <section class="card card--front" aria-label="Card front">
    <div class="brand">
      <span class="brand-mark"></span>
      <span class="brand-name">Silver Heron Construction Services</span>
    </div>
    <div class="rule-top"></div>

    <div class="person">
      <h1 class="person-name">Danielle Vesk</h1>
      <p class="person-role">Founder and CEO</p>
    </div>
    <div class="rule-mid"></div>

    <ul class="contacts">
      <li>
        <svg viewBox="0 0 14 14" aria-hidden="true"><rect x="3.5" y="0.8" width="7" height="12.4" rx="1.3" fill="none" stroke="currentColor" stroke-width="1.3"/><circle cx="7" cy="11" r="0.8" fill="currentColor"/></svg>
        303.782.4190
      </li>
      <li>
        <svg viewBox="0 0 14 14" aria-hidden="true"><rect x="0.8" y="2.5" width="12.4" height="9" fill="currentColor"/><path d="M1 3 L7 8 L13 3" fill="none" stroke="#fff" stroke-width="1.1"/></svg>
        dvesk@silverheronconst.example
      </li>
      <li>
        <svg viewBox="0 0 14 14" aria-hidden="true"><circle cx="7" cy="7" r="6" fill="none" stroke="currentColor" stroke-width="1.3"/><ellipse cx="7" cy="7" rx="2.6" ry="6" fill="none" stroke="currentColor" stroke-width="1"/><path d="M1 7 H13" stroke="currentColor" stroke-width="1"/></svg>
        www.silverheronconst.example
      </li>
    </ul>

    <address class="address" style="font-style:normal">
      4816 Alder Brook Way,<br>Ste 100 Denver, CO. 80451
    </address>

    <div class="band">Where The Road To Success Is Always Under Construction</div>
  </section>
</main>
</body>
</html>
```